BriarLoom Website Homepage Design

Please provide your idea of homepage for a hosting company. This project is for DESIGN only, no coding.

It must use/combine colors used in logo, clean, modern look.

Homepage must consist of at least 4 sections (example: testimonials, services, and so on. not necesarily all of them). We would like the navigation to be horizontal, but not mandatory.

You can include a preview of services page (optional, not a must).

Number of Pages Required

1 page

Font styles to use
Sans Serif

```html
<!DOCTYPE html>
<html lang="en">
<head>
<meta charset="utf-8">
<title>BriarLoom — Web Hosting</title>
<link href="https://fonts.googleapis.com/css2?family=Poppins:ital,wght@0,300;0,400;0,500;0,600;0,800;1,300&display=swap" rel="stylesheet">
<style>
:root{
  --blue:#0a86d8;
  --blue-soft:#5fb2ea;
  --blue-pale:#eaf4fc;
  --navy:#0b2740;
  --space:#061a2e;
  --ink:#2b2b2b;
  --muted:#6b6b6b;
  --line:#e3e8ee;
  --white:#ffffff;
  --star:#f5a623;
}
*{box-sizing:border-box;margin:0;padding:0}
html,body{width:1200px;height:3360px;overflow:hidden}
body{position:relative;font-family:"Poppins",sans-serif;color:var(--ink);background:var(--white)}
.abs{position:absolute}
.accent{color:var(--blue)}
.section-title{font-size:32px;font-weight:400;color:var(--muted)}
.section-title .accent{color:var(--blue)}

/* header */
.header{left:60px;top:0;width:1080px;height:62px;background:var(--white)}
.header::after{content:"";position:absolute;left:0;bottom:-10px;width:100%;height:10px;
  background:radial-gradient(circle at 10px 0,var(--white) 10px,transparent 11px) 0 0/20px 10px repeat-x}
.logo{left:12px;top:12px;font-size:34px;font-weight:600;color:var(--blue);letter-spacing:1px;display:flex;align-items:center;gap:8px}
.logo .dot{width:14px;height:14px;border-radius:50%;background:var(--blue)}
.nav{left:345px;top:24px;display:flex;gap:16px;font-size:11px;font-weight:500;text-transform:uppercase;color:var(--ink)}
.nav .active{color:var(--blue)}
.phone{left:842px;top:22px;font-size:16px;font-weight:600;display:flex;align-items:center;gap:6px}
.login{left:978px;top:16px;width:90px;height:34px;border-radius:17px;background:var(--blue);color:var(--white);font-size:12px;display:flex;align-items:center;justify-content:center;gap:6px}

/* hero */
.hero{left:0;top:0;width:1200px;height:760px;background:radial-gradient(ellipse at 60% 35%,#1c4b78 0%,#0d2d4d 40%,var(--space) 80%)}
.hero-tag{left:428px;top:218px;width:344px;height:36px;background:rgba(10,134,216,.55);color:var(--white);font-size:21px;font-weight:300;display:flex;align-items:center;justify-content:center}
.hero-title{left:0;top:258px;width:1200px;text-align:center;font-size:44px;font-weight:800;color:var(--white);letter-spacing:.5px}
.hero-sub{left:0;top:316px;width:1200px;text-align:center;font-size:15px;color:var(--white)}
.search{left:318px;top:356px;width:564px;height:44px;background:var(--white);border-radius:22px}
.search .ph{position:absolute;left:24px;top:14px;font-size:12px;color:#555}
.search .tld{position:absolute;left:440px;top:7px;width:76px;height:30px;border-radius:15px;background:#e8ecf0;font-size:12px;display:flex;align-items:center;justify-content:center;gap:8px}
.search .go{position:absolute;right:6px;top:6px;width:32px;height:32px;border-radius:50%;background:var(--blue);display:flex;align-items:center;justify-content:center}
.tld-label{font-size:19px;color:var(--blue)}
.hero-robot{left:818px;top:352px;width:282px;height:380px;border-radius:48% 48% 40% 40%;background:radial-gradient(circle at 45% 30%,#ffffff,#cfd8e0 60%,#8a99a8)}

/* about */
.about-badge{left:246px;top:686px;width:190px;height:190px;border-radius:50%;background:#f4f8fc}
.about-title{left:219px;top:756px;font-size:34px;font-weight:400;color:var(--muted)}
.about-text{left:590px;top:760px;width:400px}
.about-text .lead{font-size:13px;line-height:21px;color:#444;margin-bottom:12px}
.about-text .body{font-size:10px;line-height:19.5px;color:#666}
.about-text .more{display:flex;align-items:center;gap:6px;margin-top:18px;font-size:12px;color:var(--blue);text-decoration:underline}

/* plans */
.plans{left:0;top:1000px;width:1200px;height:670px;background:linear-gradient(#fff,var(--blue-pale))}
.plans-head{left:0;top:1052px;width:1200px;text-align:center}
.plans-head p{font-size:12.5px;line-height:21px;color:#555;width:460px;margin:14px auto 0}
.card{background:var(--white);border:1px solid #d7e6f3;overflow:hidden}
.card h3{height:62px;display:flex;align-items:center;justify-content:center;font-size:16px;font-weight:500}
.card .price{height:46px;background:var(--blue-soft);color:var(--white);font-size:23px;font-weight:300;display:flex;align-items:center;justify-content:center}
.card.featured{border-color:var(--blue);box-shadow:0 4px 18px rgba(10,134,216,.18)}
.card.featured .price{height:82px;background:var(--blue);flex-direction:column;font-weight:600}
.card.featured .price small{font-size:10px;font-weight:400;margin-top:4px}
.specs{list-style:none;margin:20px 26px 0}
.specs li{display:flex;justify-content:space-between;font-size:11px;height:32px;align-items:center;border-bottom:1px solid var(--line)}
.specs li span:last-child{color:var(--blue)}
.btn{display:flex;align-items:center;justify-content:center;width:142px;height:36px;border-radius:18px;background:var(--blue);color:var(--white);font-size:13px;margin:30px auto 0}
.card svg.wave{position:absolute;left:0;bottom:0}

/* services */
.service-robot{left:176px;top:1738px;width:200px;height:282px;border-radius:45% 45% 30% 30%;background:radial-gradient(circle at 45% 30%,#ffffff,#d3dbe3 60%,#9aa7b4)}
.services-title{left:462px;top:1762px}
.services-title p{font-size:12.5px;color:#555;margin-top:4px}
.service{width:117px;height:117px;border-radius:50%;background:var(--blue);border:4px solid var(--white);box-shadow:0 0 0 2px #b8d8f0;color:var(--white);font-size:13px;line-height:16px;text-align:center;display:flex;flex-direction:column;align-items:center;justify-content:center;gap:6px}

/* reviews */
.reviews-bg{left:0;top:1990px;width:1200px;height:640px}
.reviews-head{left:0;top:2166px;width:1200px;text-align:center}
.reviews-head p{font-size:13px;margin-top:6px}
.stars{left:545px;top:2255px;display:flex;gap:3px}
.avatar{width:75px;height:75px;border-radius:50%;background:linear-gradient(#b08a6e,#6b4a3a)}
.quote{width:357px;height:156px;background:var(--white);padding:22px 32px}
.quote p{font-size:11px;font-style:italic;font-weight:300;line-height:20px;color:#555}
.quote .who{margin-top:14px;font-size:11px;display:flex;align-items:center;gap:6px}
.quote .who::before{content:"";width:12px;height:1px;background:var(--blue)}
.slider-line{height:1px;background:var(--blue);top:2530px}
.arrow-btn{width:33px;height:33px;border:1px solid var(--blue);background:var(--white);display:flex;align-items:center;justify-content:center;top:2514px}

/* newsletter */
.news-head{left:0;top:2702px;width:1200px;text-align:center}
.news-head p{font-size:13px;margin-top:6px}
.email{left:356px;top:2796px;width:488px;height:42px;border:1px solid #d6dde4;border-radius:21px;font-size:11px;color:#777;padding:13px 20px}
.subscribe{left:356px;top:2849px;width:488px;height:42px;border-radius:21px;background:var(--blue);color:var(--white);font-size:14px;display:flex;align-items:center;justify-content:center}
.news-robot{left:905px;top:2655px;width:230px;height:340px;border-radius:45% 45% 30% 30%;background:radial-gradient(circle at 45% 30%,#ffffff,#d3dbe3 60%,#9aa7b4)}

/* footer */
.footer-col h4{font-size:16px;font-weight:400;color:var(--white);margin-bottom:10px}
.footer-col ul{list-style:none;font-size:11px;line-height:22.5px;color:#c9d6e2}
.footer-col.left li::before{content:"▲";color:var(--blue);font-size:6px;margin-right:10px;vertical-align:2px}
.footer-col.right{text-align:right}
.footer-col.right li::after{content:"▲";color:var(--blue);font-size:6px;margin-left:10px;vertical-align:2px}
.footer-logo{left:0;top:3118px;width:1200px;display:flex;justify-content:center;align-items:center;gap:8px;font-size:36px;font-weight:600;color:var(--blue)}
.footer-logo .dot{width:14px;height:14px;border-radius:50%;background:var(--blue)}
.socials{left:544px;top:3180px;display:flex;gap:8px}
.socials span{width:32px;height:32px;border-radius:50%;border:2px solid var(--blue)}
.contact{left:0;top:3236px;width:1200px;display:flex;justify-content:center;gap:30px;font-size:13px;color:var(--white)}
.contact span{display:flex;align-items:center;gap:8px}
.copyright{left:0;top:3312px;width:1200px;height:48px;background:var(--blue);color:var(--white);font-size:11px;display:flex;align-items:center;justify-content:center}
</style>
</head>
<body>

<!-- hero -->
<div class="abs hero"></div>
<span class="abs tld-label" style="left:610px;top:440px">.org</span>
<span class="abs tld-label" style="left:522px;top:498px">.net</span>
<span class="abs tld-label" style="left:346px;top:534px">.com</span>
<span class="abs tld-label" style="left:732px;top:522px">.in</span>
<span class="abs tld-label" style="left:828px;top:530px">.ca</span>
<svg class="abs" style="left:0;top:440px" width="1200" height="320" viewBox="0 0 1200 320">
  <path fill="#ffffff" d="M0 150 C180 150 330 140 470 190 C620 245 780 250 930 215 C1060 185 1140 230 1200 290 L1200 320 L0 320Z"/>
  <path fill="#0a86d8" d="M0 28 C70 0 150 40 138 120 C128 190 60 220 0 320Z"/>
</svg>
<div class="abs hero-robot" role="img" aria-label="Illustration of a white flying robot waving"></div>

<header class="abs header">
  <div class="abs logo"><span class="dot"></span>BriarLoom</div>
  <nav class="abs nav">
    <span class="active">Home</span><span>Services</span><span>Price and Plan</span><span>Testimonials</span><span>Contact Us</span>
  </nav>
  <div class="abs phone">
    <svg width="16" height="16" viewBox="0 0 24 24"><path fill="#0a86d8" d="M6.6 10.8a15 15 0 0 0 6.6 6.6l2.2-2.2a1 1 0 0 1 1-.25 11.4 11.4 0 0 0 3.6.57 1 1 0 0 1 1 1V20a1 1 0 0 1-1 1A17 17 0 0 1 3 4a1 1 0 0 1 1-1h3.5a1 1 0 0 1 1 1c0 1.25.2 2.45.57 3.57a1 1 0 0 1-.25 1z"/></svg>
    555 014 2290
  </div>
  <div class="abs login">
    <svg width="14" height="14" viewBox="0 0 24 24" fill="none" stroke="#fff" stroke-width="2"><circle cx="12" cy="12" r="10"/><path d="M8 12h8M13 8l4 4-4 4"/></svg>
    LOGIN
  </div>
</header>

<div class="abs hero-tag">FLY WITH THE BEST HOSTING</div>
<h1 class="abs hero-title">WE PROVIDE WEB HOSTING</h1>
<p class="abs hero-sub">The optimal Solution for fast, Reliable Websites</p>
<div class="abs search">
  <span class="ph">Enter Your Domain Name</span>
  <span class="tld">.com <svg width="8" height="5"><path d="M0 0h8L4 5z" fill="#333"/></svg></span>
  <span class="go"><svg width="14" height="14" viewBox="0 0 24 24" fill="none" stroke="#fff" stroke-width="3"><circle cx="10" cy="10" r="7"/><path d="M15 15l6 6"/></svg></span>
</div>

<!-- about -->
<div class="abs about-badge"></div>
<h2 class="abs about-title"><span class="accent">About</span> BriarLoom</h2>
<div class="abs about-text">
  <p class="lead">Lorem Ipsum has been the industry's standard dummy text ever since an unknown printer galley.</p>
  <p class="body">Lorem Ipsum has been the industry's standard dummy text ever since the 1500s, when an unknown printer took a galley of type and scrambled it to make a type specimen book. It has survived not only five centuries, but also the leap into electronic.</p>
  <span class="more">Learn More <svg width="14" height="14" viewBox="0 0 24 24"><circle cx="12" cy="12" r="12" fill="#0a86d8"/><path d="M10 7l5 5-5 5" stroke="#fff" stroke-width="2.5" fill="none"/></svg></span>
</div>

<!-- plans -->
<div class="abs plans"></div>
<div class="abs plans-head">
  <h2 class="section-title"><span class="accent">Plan &amp;</span> Price</h2>
  <p>Lorem Ipsum has been the industry's standard dummy text ever since an unknown printer took a galley of type and</p>
</div>

<article class="abs card" style="left:196px;top:1209px;width:269px;height:373px">
  <h3>Shared Hosting</h3>
  <div class="price">$299/mo</div>
  <ul class="specs"><li><span>Disk Space</span><span>250 GB</span></li><li><span>Data Bandwidth</span><span>1 TB</span></li><li><span>Email Accounts</span><span>120</span></li><li><span>LTDs Domains</span><span>50</span></li></ul>
  <span class="btn">GET STARTED</span>
  <svg class="wave" width="269" height="44" viewBox="0 0 269 44"><path fill="#d3e8f8" d="M0 14 C60 0 110 30 170 20 C220 12 240 6 269 14 L269 44 L0 44Z"/><path fill="#b5d9f4" d="M0 30 C70 20 130 40 200 28 C235 22 255 24 269 28 L269 44 L0 44Z"/></svg>
</article>

<article class="abs card featured" style="left:465px;top:1178px;width:270px;height:413px">
  <h3>Dedicated Servers</h3>
  <div class="price">$355/mo<small>Lorem Ipsum has been the indus</small></div>
  <ul class="specs"><li><span>Disk Space</span><span>500 GB</span></li><li><span>Data Bandwidth</span><span>2 TB</span></li><li><span>Email Accounts</span><span>150</span></li><li><span>LTDs Domains</span><span>75</span></li></ul>
  <span class="btn">GET STARTED</span>
  <svg class="wave" width="270" height="44" viewBox="0 0 270 44"><path fill="#b5d9f4" d="M0 14 C60 0 110 30 170 20 C220 12 240 6 270 14 L270 44 L0 44Z"/><path fill="#7fc0ec" d="M0 30 C70 20 130 40 200 28 C235 22 255 24 270 28 L270 44 L0 44Z"/></svg>
</article>

<article class="abs card" style="left:735px;top:1209px;width:269px;height:373px">
  <h3>VPS Hosting</h3>
  <div class="price">$455/mo</div>
  <ul class="specs"><li><span>Disk Space</span><span>750 GB</span></li><li><span>Data Bandwidth</span><span>5 TB</span></li><li><span>Email Accounts</span><span>500</span></li><li><span>LTDs Domains</span><span>100</span></li></ul>
  <span class="btn">GET STARTED</span>
  <svg class="wave" width="269" height="44" viewBox="0 0 269 44"><path fill="#d3e8f8" d="M0 14 C60 0 110 30 170 20 C220 12 240 6 269 14 L269 44 L0 44Z"/><path fill="#b5d9f4" d="M0 30 C70 20 130 40 200 28 C235 22 255 24 269 28 L269 44 L0 44Z"/></svg>
</article>

<!-- reviews background with wave top -->
<svg class="abs reviews-bg" width="1200" height="640" viewBox="0 0 1200 640">
  <path fill="#eef6fd" d="M0 0 C180 80 320 120 460 112 C620 102 760 55 900 40 C1040 25 1130 10 1200 0 L1200 640 L0 640Z"/>
</svg>

<!-- services -->
<div class="abs service-robot" role="img" aria-label="Illustration of a robot touching a holographic screen"></div>
<div class="abs services-title">
  <h2 class="section-title"><span class="accent">Services</span> We Provide</h2>
  <p>Lorem Ipsum has been the industry's standard dummy text ever !</p>
</div>
<div class="abs service" style="left:452px;top:1856px">
  <svg width="34" height="30" viewBox="0 0 34 30" fill="none" stroke="#fff" stroke-width="1.8"><rect x="2" y="2" width="30" height="8"/><rect x="2" y="12" width="30" height="8"/><rect x="2" y="22" width="30" height="6"/></svg>
  Dedicated<br>Server
</div>
<div class="abs service" style="left:602px;top:1856px">
  <svg width="34" height="30" viewBox="0 0 34 30" fill="none" stroke="#fff" stroke-width="1.8"><circle cx="11" cy="10" r="7"/><rect x="16" y="12" width="16" height="6"/><rect x="16" y="20" width="16" height="6"/></svg>
  VPS<br>Hosting
</div>
<div class="abs service" style="left:752px;top:1856px">
  <svg width="34" height="30" viewBox="0 0 34 30" fill="none" stroke="#fff" stroke-width="1.8"><rect x="2" y="2" width="30" height="24"/><circle cx="20" cy="15" r="7"/></svg>
  Domain<br>Investing
</div>
<div class="abs service" style="left:902px;top:1856px">
  <svg width="34" height="30" viewBox="0 0 34 30" fill="none" stroke="#fff" stroke-width="1.8"><path d="M9 10a8 7 0 0 1 16 0"/><rect x="6" y="12" width="22" height="6"/><rect x="6" y="20" width="22" height="6"/></svg>
  Cloud<br>Reseller
</div>
<svg class="abs" style="left:1064px;top:1890px" width="18" height="46" viewBox="0 0 18 46"><path d="M2 2l14 21L2 44" fill="none" stroke="#333" stroke-width="1.5"/></svg>

<!-- reviews -->
<div class="abs reviews-head">
  <h2 class="section-title"><span class="accent">Happy Client</span> Reviews</h2>
  <p>People Like You Already Enjoy Web Hosting</p>
</div>
<div class="abs stars">
  <svg width="110" height="18" viewBox="0 0 110 18" fill="#f5a623"><g id="s"><path d="M9 0l2.6 5.8 6.4.6-4.8 4.2 1.4 6.3L9 13.6 3.4 16.9l1.4-6.3L0 6.4l6.4-.6z"/></g><use href="#s" x="22"/><use href="#s" x="44"/><use href="#s" x="66"/><use href="#s" x="88"/></svg>
</div>

<div class="abs avatar" style="left:133px;top:2323px" role="img" aria-label="Client portrait photo"></div>
<div class="abs quote" style="left:228px;top:2312px">
  <p>Lorem Ipsum has been the industry's standard dummy text ever since the 1500s, when an unknown printer took a galley of type and scrambled it to make a type specimen book.</p>
  <div class="who"><span class="accent">Client Name</span> (something.com)</div>
</div>
<div class="abs avatar" style="left:610px;top:2323px" role="img" aria-label="Client portrait photo"></div>
<div class="abs quote" style="left:707px;top:2312px">
  <p>Lorem Ipsum has been the industry's standard dummy text ever since the 1500s, when an unknown printer took a galley of type and scrambled it to make a type specimen book.</p>
  <div class="who"><span class="accent">Client Name</span> (something.com)</div>
</div>
<div class="abs slider-line" style="left:135px;width:418px"></div>
<div class="abs slider-line" style="left:648px;width:418px"></div>
<div class="abs arrow-btn" style="left:563px"><svg width="10" height="14"><path d="M8 1L2 7l6 6" fill="none" stroke="#0a86d8" stroke-width="2"/></svg></div>
<div class="abs arrow-btn" style="left:604px;border-color:#333"><svg width="10" height="14"><path d="M2 1l6 6-6 6" fill="none" stroke="#333" stroke-width="2"/></svg></div>

<!-- footer background -->
<svg class="abs" style="left:0;top:2880px" width="1200" height="432" viewBox="0 0 1200 432">
  <path fill="#0b2740" d="M0 20 C150 60 250 120 380 112 C520 104 620 60 760 62 C880 64 960 120 1060 110 C1130 104 1170 80 1200 70 L1200 432 L0 432Z"/>
</svg>
<svg class="abs" style="left:940px;top:2930px" width="260" height="140" viewBox="0 0 260 140"><ellipse cx="160" cy="70" rx="212" ry="62" fill="#0a86d8"/></svg>
<svg class="abs" style="left:212px;top:2978px" width="44" height="40" viewBox="0 0 44 40"><rect x="2" y="2" width="28" height="20" rx="8" fill="#0a86d8"/><rect x="14" y="12" width="28" height="20" rx="8" fill="#3fa3e6"/><path d="M8 10h16M8 15h10" stroke="#fff" stroke-width="2"/></svg>

<!-- newsletter -->
<div class="abs news-head">
  <h2 class="section-title"><span class="accent">Stay Upto</span> Date With Us!</h2>
  <p>Would you like to receive our exclusive update for signup !</p>
</div>
<div class="abs email">Enter Email *</div>
<div class="abs subscribe">SUBSCRIBE</div>
<div class="abs news-robot" role="img" aria-label="Illustration of a cheering robot standing on a platform"></div>

<!-- footer -->
<div class="abs footer-col left" style="left:70px;top:3104px">
  <h4><span class="accent">Com</span>pany</h4>
  <ul><li>Home</li><li>Services</li><li>Price and Plan</li><li>Testimonials</li><li>Contact Us</li></ul>
</div>
<div class="abs footer-col right" style="right:70px;top:3104px">
  <h4><span class="accent">Hos</span>ting</h4>
  <ul><li>Dedicated Server</li><li>Business Hosting</li><li>Web Hosting</li><li>VPS Hosting</li><li>Domain Investing</li><li>Cloud Reseller</li></ul>
</div>
<div class="abs footer-logo"><span class="dot"></span>BriarLoom</div>
<div class="abs socials"><span></span><span></span><span></span></div>
<div class="abs contact">
  <span><svg width="14" height="14" viewBox="0 0 24 24"><path fill="#0a86d8" d="M6.6 10.8a15 15 0 0 0 6.6 6.6l2.2-2.2a1 1 0 0 1 1-.25 11.4 11.4 0 0 0 3.6.57 1 1 0 0 1 1 1V20a1 1 0 0 1-1 1A17 17 0 0 1 3 4a1 1 0 0 1 1-1h3.5a1 1 0 0 1 1 1c0 1.25.2 2.45.57 3.57a1 1 0 0 1-.25 1z"/></svg>555 014 2290</span>
  <span><svg width="16" height="12" viewBox="0 0 16 12" fill="none" stroke="#0a86d8" stroke-width="1.5"><rect x="1" y="1" width="14" height="10"/><path d="M1 1l7 6 7-6"/></svg>hello@briarloom.test</span>
</div>
<div class="abs copyright">©BRIARLOOM -2021 All rights reserved. Privacy Policy &nbsp;|&nbsp; Tearms &amp; Condition</div>

</body>
</html>
```